Fresh and Trendy Daily Deals Aggregator in 17 countries in Europe needs your web design inspiration to inspire the buying masses. We are a young, fresh, crazy and dynamic team and we plan to take the daily deals space by storm very soon. tukamoro will bring a completely fresh approach to giving people amazing discount offers from daily deal sites, such as Velmora, HarborFinch and others for things like spa treatments, fitness, clubs, restaurants, online shopping, offers, health, beauty... Be a part of a happening!

We are looking for a web design with no coding for an ajax-based website (we need PSD, no HTML/CSS). We are looking for something that will look fresh and not too techy. Needs to be very readable - so a nice contrast between font and background and a readable font. We really like the simplicity of quorra, plinket: light, fun, simple to read, modern, minimalist, easy to navigate.

We also like the following landers:

Quorra (Simple colors and easy to navigate)
HarborFinch.com (nice image as the background)
Velmora.com (Simple colors and easy to navigate)
http://mintoraspotlane.com/ (Nice site ambience and nice skin)
http://www.789vrak.fr/city,paris,tous-les-bons-plans.html (Map View with little deal icons showing the location and type of deal)
http://www.kelvostrand.com (Map View with little deal icons showing the location and type of deal)

We want something hip and trendy, fun and fresh but DIFFERENT from all the rest out there. We'd also want to keep the number of user clicks to the bare minimum possible.

Reason: Hello! Since most of the designs are still going through revisions we've decided to extend the deadline to give everybody the best chance of completing their designs. Thanks so far for all the great designs! Osvin TUKAMORO

Target Market(s)

Our target audience is: Trendy, active people who like to go out several times per week, they have money, educated, between 18 and 40 years old and fa

Industry/Entity Type

Fitness

Requirements
Must have
• Design Specs:

- MUST HAVE ALL THE FILTERS SEEN ON OUR TEST SITE (see below for URL and login details)
- MUST BE ABLE TO SEE LOTS OF DEALS PER PAGE BECAUSE WE ARE A DAILY DEALS AGGREGATOR AND HAVE HUNDREDS OF DEALS.
- The width needs to be a size that will work with every size computer screen
* Need to use cross-platform compatible font (Google webfonts ok)
- The graphic elements used for the design must be copyright free

You can find our current test site here:

http://rmt.brovika-tessel.com

Username: makers@brovika-tessel.com
Password: 47quills

This is a very basic version, all functionnalities are not working yet, and we are looking to you to make it all make graphical sense to the user so that it's ultra easy to understand and to navigate through.

Our Logo has been uploaded as PSD files with all the color variations. Please base the color scheme of the site on the colors of the logo but feel free to use lighter or darker shades of the same colors as well as black, grays or white, if necessary.

The CMYK for each color is:

Green: C40 & Y100
Pink: M86

Be creative and refer often back to the web 2.0 landers above.

IMPORTANT NOTES REGARDING OUR CURRENT TEST SITE:
Fell free to group elements differently or to hide them under pop- ups, to resize them or to change them in any way that works with your design. The only constraint is that all of the functions must be easily accessible to the user.

We would like to have little icons signifying each category. On our test site, all the categories might not be visible but the categories are: Dining, Health & Beauty, Style, Nightlife, Education & Training, Shopping, Travel, Special Interest, Events, Services, Fitness, Other.

The second tab of the site is a map view and we'd like the little category icons to be used as the points that show where the deals are located and the kind of deals that are located there. (For regerence see http://www.kelvostrand.com/#DynamicContentContainer AND http://www.789vrak.fr/city,paris,tous-les-bons-plans.html)

Tukamoro is currently aggregating deals from 17 European countries and we need to make it easy for the user to navigate from one country to another.

On our test site you will see country flags at the top of the page. If we could have the name of each country next to its flag without sacrificing too much space it would be better. But, if you find an even better way to make this work feel free to do so. Also, at the bottom of the page we have all the cities in which we have deals, and the list gets very long. If you could design another way to let the user see the countries/cities/deals via the bottom page links it would save space.

Also, when you log in to our test site you will see a pop-up. The text of the pop-up should only be: "Let TukaMoro save you precious time and find your perfect deals so you can sit back, relax and enjoy. Tell us what you like and how you like it and we'll deliver personalized deals right to your inbox. Or use our convenient selectors to see all the deals that are just right for you."

Finally, the banner at the top of the page that reads: "SELL ONLINE" should say: "Sell your own deals through TukaMoro!

Accepted file formats: During the design phase adobe PSD and JPEG are OK (if you need to upload files), but for the handover we'll need PSD only with all the original layers.

```html
<!DOCTYPE html>
<html lang="en">
<head>
<meta charset="utf-8">
<title>TukaMoro – Daily Deals</title>
<link rel="stylesheet" href="https://fonts.googleapis.com/css2?family=Arimo:wght@400;700&family=Signika:wght@300;400&family=Gelasio:wght@400&display=swap">
<style>
:root{
  --pink:#d0104f;
  --pink-dark:#9c0a3a;
  --green:#9acd32;
  --green-dark:#6a9a12;
  --lime-btn:#7cc11e;
  --ink:#222;
  --muted:#555;
  --footer:#231f20;
  --footer-text:#cfcfcf;
  --field:#f1f1f1;
  --sky-top:#86aedb;
  --sky-mid:#b9d3ee;
  --sand:#e6dfd2;
}
*{box-sizing:border-box;margin:0;padding:0}
html,body{width:1097px;height:1200px;overflow:hidden}
body{
  position:relative;
  font-family:"Arimo",Arial,sans-serif;
  color:var(--ink);
  background:
    radial-gradient(ellipse 260px 120px at 90px 330px,rgba(255,255,255,.85),transparent 70%),
    radial-gradient(ellipse 200px 110px at 1030px 320px,rgba(255,255,255,.8),transparent 70%),
    radial-gradient(ellipse 230px 140px at 80px 700px,rgba(255,255,255,.75),transparent 70%),
    linear-gradient(180deg,var(--sky-top) 0,var(--sky-mid) 780px,#d9e4ee 860px,var(--sand) 900px,#efe9de 1200px);
}
.abs{position:absolute}

/* header */
.brand{left:176px;top:18px;display:flex;align-items:center;gap:10px}
.brand-dot{width:40px;height:40px;border-radius:50%;background:var(--green)}
.brand-name{font-family:"Signika",sans-serif;font-weight:400;font-size:40px;color:#e0189a;line-height:1}
.flags{left:408px;top:9px;display:flex;gap:5px}
.flags span{display:block;width:12px;height:11px;border:1px solid rgba(0,0,0,.15)}
.home-btn{left:873px;top:5px;width:38px;height:38px;border-radius:50%;
  background:radial-gradient(circle at 50% 35%,#8fd0ff,#1c6fc4 70%);border:2px solid #fff;box-shadow:0 1px 3px rgba(0,0,0,.3)}
.home-btn svg{position:absolute;left:8px;top:7px}
.search-label{left:408px;top:47px;color:#fff;font-family:"Signika",sans-serif;font-weight:300;font-size:15px}
.search-input{left:461px;top:45px;width:178px;height:22px;background:#fff;border-radius:4px}
.search-btn{left:644px;top:45px;width:72px;height:22px;border-radius:4px;background:linear-gradient(#8fd43a,#4f9a0f);
  color:#123;font-family:"Signika",sans-serif;font-weight:300;font-size:14px;text-align:center;line-height:20px;border:1px solid #3f7a0a}
.signup-field{left:767px;top:61px;width:152px;height:16px;background:#111;color:#ddd;font-size:9px;line-height:16px;padding-left:9px}
.signup-note{left:772px;top:80px;width:140px;color:#fff;font-size:7.5px;line-height:8px}

.view-tabs{left:405px;top:90px;width:326px;height:44px;border-radius:6px;background:linear-gradient(#555,#1c1c1c);
  display:flex;align-items:center;justify-content:center;gap:16px;font-family:"Signika",sans-serif;font-weight:300;font-size:14px;color:#fff;
  box-shadow:0 3px 4px rgba(0,0,0,.35);z-index:2}
.view-tabs .active{color:#b6e04a}

/* hero */
.hero{left:156px;top:105px;width:785px;height:297px;background:var(--green);box-shadow:0 2px 4px rgba(0,0,0,.2)}
.hero-pin{left:27px;top:75px}
.hero-title{left:68px;top:73px;font-family:"Signika",sans-serif;font-weight:300;font-size:32px;line-height:38px;color:#b2102f}
.hero-text{left:72px;top:156px;width:250px;font-family:"Signika",sans-serif;font-weight:300;font-size:13.5px;line-height:17px;color:#1e2a10}
.hero-art{left:372px;top:36px;width:390px;height:246px;border-radius:6px;
  background:linear-gradient(160deg,#dcdcdc,#a8b79a)}
.hero-dots{left:184px;top:270px;display:flex;gap:10px}
.hero-dots span{width:15px;height:15px;border-radius:50%;background:#fff}
.hero-dots .on{background:#b2102f}

/* ribbons */
.ribbon{height:46px;background:linear-gradient(#e0245f,var(--pink-dark));color:#fff;font-family:"Gelasio",serif;font-weight:400;font-size:18px;line-height:40px}
.ribbon-left{left:152px;top:415px;width:388px;padding-left:27px;clip-path:polygon(0 0,100% 0,92% 50%,100% 100%,0 100%)}
.ribbon-left .pin{position:absolute;left:322px;top:5px;width:29px;height:29px;border-radius:50%;background:#fff}
.ribbon-left .pin svg{position:absolute;left:8px;top:6px}
.ribbon-right{left:708px;width:236px;padding-left:56px;clip-path:polygon(0 0,100% 0,100% 100%,0 92%,6% 46%)}
.ribbon-right::after{content:"";position:absolute;right:0;top:0;width:4px;height:100%;background:var(--pink-dark)}

/* deals */
.deal{left:178px;width:498px;height:182px}
.deal-photo{position:absolute;left:0;top:8px;width:140px;height:150px;
  background:linear-gradient(135deg,#e9d7ae,#c9b182);box-shadow:0 2px 4px rgba(0,0,0,.25)}
.deal-photo i{position:absolute;left:20px;top:22px;width:98px;height:85px;background:linear-gradient(135deg,#4d7a3e,#f3f0e6 55%,#d8a85b)}
.deal-caption{position:absolute;left:27px;top:111px;font-size:7.5px;line-height:9px;color:#8a2a12;text-decoration:underline}
.deal-badge{position:absolute;left:90px;top:90px;width:70px;height:70px;border-radius:50%;background:#fff;box-shadow:0 2px 4px rgba(0,0,0,.35)}
.deal-badge b{position:absolute;left:5px;top:5px;width:60px;height:60px;border-radius:50%;background:radial-gradient(circle at 40% 35%,#f47a8a,#d1203d);
  color:#fff;font-family:"Signika",sans-serif;font-weight:400;font-size:23px;line-height:60px;text-align:center}
.deal-desc{position:absolute;left:165px;top:11px;width:310px;font-size:9.5px;line-height:13px;color:#222}
.deal-desc strong{color:#000}
.deal-heading{position:absolute;left:165px;top:60px;font-family:"Gelasio",serif;font-weight:400;font-size:14px;color:#6b3a1a}
.deal-link{position:absolute;left:165px;width:307px;font-size:8px;font-weight:700;color:#b01a1a;padding-left:15px;border-bottom:1px dotted #b6d36a;height:14px}
.deal-link::before{content:"";position:absolute;left:1px;top:2px;width:5px;height:5px;border:1px solid #444;border-radius:50%}
.deal-timer{position:absolute;left:182px;top:128px;font-size:14px;color:#222}
.deal-timer small{font-size:8px}
.deal-btn{position:absolute;left:347px;top:121px;width:133px;height:26px;border-radius:5px;background:linear-gradient(#fff,#e8e8e8);
  border:1px solid #c9c9c9;color:#8bc53a;font-family:"Signika",sans-serif;font-weight:300;font-size:17px;text-align:center;line-height:24px}
.deal-sep{position:absolute;left:0;top:174px;width:498px;border-top:1px dashed #999}

.divider{left:689px;top:425px;height:300px;border-left:1px dotted #b8c66a}

/* pagination */
.pager{left:178px;top:1013px;height:24px}
.pager span{position:absolute;top:0;height:24px;border-radius:4px;background:linear-gradient(#fff,#d8d8d8);border:1px solid #bbb;
  font-size:10px;font-weight:700;color:#555;text-align:center;line-height:22px}
.pager .current{background:linear-gradient(#aaa,#777);color:#333}

/* sidebar */
.cat-list{left:724px;top:449px;width:202px;list-style:none}
.cat-list li{height:32px;border-bottom:1px dotted #888;font-family:"Signika",sans-serif;font-weight:300;font-size:14px;color:#222;display:flex;align-items:center;gap:15px;padding-left:10px}
.cat-list li:last-child{border-bottom:0}
.cat-icon{width:16px;height:16px;border-radius:50%}
.field{background:var(--field);font-size:9px;color:#222;padding-left:6px;border:1px solid #e2e2e2}
.select::after{content:"";position:absolute;right:8px;top:5px;border:4px solid transparent;border-top:5px solid var(--pink)}
.slider{height:10px;border-radius:5px;background:#111}
.slider::before,.slider::after{content:"";position:absolute;top:2px;width:6px;height:6px;border-radius:50%;border:1px solid #888}
.slider::before{left:3px}.slider::after{right:3px}
.slider i{position:absolute;left:12px;top:4px;width:46px;height:2px;background:#555}
.small-label{font-size:9px;color:#222}
.tiny-btn{border-radius:8px;background:linear-gradient(#fff,#ddd);border:1px solid #aaa;font-size:8.5px;text-align:center;line-height:11px}
.placeholder{color:#aaa}
.go-btn{left:886px;top:1013px;width:30px;height:30px;border-radius:50%;background:linear-gradient(#fff,#ddd);border:1px solid #999;font-size:13px;text-align:center;line-height:28px}

/* footer */
.site-footer{left:156px;top:1053px;width:785px;height:147px;background:var(--footer)}
.foot-col{position:absolute;top:21px}
.foot-col h4{font-size:11px;font-weight:400;color:#fff;letter-spacing:.3px;margin-bottom:6px}
.foot-col li{list-style:none;font-size:8.5px;line-height:14px;color:var(--footer-text)}
.social{display:flex;gap:6px;margin-top:8px}
.social span{width:22px;height:22px;border-radius:50%}
.news-input{position:absolute;left:597px;top:44px;width:153px;height:17px;background:#fff}
.news-btn{position:absolute;left:639px;top:68px;width:64px;height:18px;border-radius:9px;background:linear-gradient(#a6e04a,#5ea014);
  color:#123;font-size:12px;text-align:center;line-height:18px}
.copyright{position:absolute;left:605px;top:122px;font-size:8.5px;color:#bbb}
</style>
</head>
<body>

<header>
  <div class="abs brand"><span class="brand-dot"></span><span class="brand-name">tukamoro</span></div>
  <div class="abs flags" aria-label="Country selector">
    <span style="background:linear-gradient(90deg,#2a9b3f 33%,#fff 33% 66%,#d22 66%)"></span>
    <span style="background:linear-gradient(#9e2a2f 40%,#fff 40% 60%,#9e2a2f 60%)"></span>
    <span style="background:linear-gradient(#c33 33%,#fff 33% 66%,#c33 66%)"></span>
    <span style="background:linear-gradient(#fdb913 33%,#006a44 33% 66%,#c1272d 66%)"></span>
    <span style="background:linear-gradient(#ed2939 33%,#fff 33% 66%,#00a1de 66%)"></span>
    <span style="background:linear-gradient(90deg,#fff 50%,#d22 50%)"></span>
    <span style="background:linear-gradient(90deg,#0046ae 33%,#ffd200 33% 66%,#cc092f 66%)"></span>
    <span style="background:linear-gradient(#fff 50%,#dc143c 50%)"></span>
    <span style="background:linear-gradient(#0072ce 33%,#000 33% 66%,#fff 66%)"></span>
    <span style="background:linear-gradient(#fff 40%,#003580 40% 60%,#fff 60%)"></span>
    <span style="background:linear-gradient(90deg,#002395 33%,#fff 33% 66%,#ed2939 66%)"></span>
    <span style="background:linear-gradient(#c8102e 40%,#fff 40% 60%,#c8102e 60%)"></span>
    <span style="background:repeating-linear-gradient(#0d5eaf 0 1.3px,#fff 1.3px 2.6px)"></span>
    <span style="background:linear-gradient(#ce2939 33%,#fff 33% 66%,#477050 66%)"></span>
    <span style="background:linear-gradient(90deg,#009246 33%,#fff 33% 66%,#ce2b37 66%)"></span>
    <span style="background:linear-gradient(#02529c 40%,#dc1e35 40% 60%,#02529c 60%)"></span>
  </div>
  <div class="abs home-btn"><svg width="18" height="18" viewBox="0 0 18 18"><path d="M9 2 1 9h2v7h4v-5h4v5h4V9h2z" fill="#fff"/></svg></div>
  <div class="abs search-label">Search</div>
  <div class="abs search-input"></div>
  <div class="abs search-btn">Search</div>
  <div class="abs signup-field">Your e-mail Address</div>
  <div class="abs signup-note">Sign up and get all deals you really want just the way you want them!</div>
  <nav class="abs view-tabs"><span class="active">List View</span><span>|</span><span>Map View</span><span>|</span><span>Previous Deals</span></nav>
</header>

<section class="abs hero">
  <svg class="abs hero-pin" width="32" height="40" viewBox="0 0 32 40"><path d="M16 1C8 1 2 7 2 15c0 10 14 24 14 24s14-14 14-24C30 7 24 1 16 1z" fill="#2b2b2b"/><circle cx="16" cy="15" r="5" fill="#9acd32"/></svg>
  <h1 class="abs hero-title">Sell your own deals<br>through TukaMoro!</h1>
  <p class="abs hero-text">Lorem Ipsum is simply dummy text of the printing and typesetting industry. Lorem Ipsum has been the industry's standard dummy text</p>
  <div class="abs hero-art" role="img" aria-label="Illustration of a folded world map with a large location pin"></div>
  <div class="abs hero-dots"><span></span><span></span><span></span><span class="on"></span></div>
</section>

<main>
  <h2 class="abs ribbon ribbon-left">Our Spectrum of Services
    <span class="pin"><svg width="13" height="17" viewBox="0 0 13 17"><path d="M6.5 0C3 0 0 2.8 0 6.3 0 11 6.5 17 6.5 17S13 11 13 6.3C13 2.8 10 0 6.5 0z" fill="#d0104f"/><circle cx="6.5" cy="6.3" r="2.4" fill="#fff"/></svg></span>
  </h2>

  <article class="abs deal" style="top:455px">
    <div class="deal-photo" role="img" aria-label="Photo of white magnolia flowers in a torn paper frame"><i></i><span class="deal-caption">Cras turpis duis a<br>eget nulla vulput</span></div>
    <div class="deal-badge"><b>50%</b></div>
    <p class="deal-desc"><strong>Donec accumsan porta risus.</strong> Vestibulum sollicitudinlibero ut semper commodo, purus enim sollicitudin nulla, dictum vehicula diam lacus at purus. In egestas.</p>
    <h3 class="deal-heading">Services</h3>
    <div class="deal-link" style="top:82px">Nam congue quam non augue ivamus porttitor</div>
    <div class="deal-link" style="top:100px">Jam aongue buam n augue famus</div>
    <div class="deal-timer">30 : 15 : 15 : 06 <small>ago</small></div>
    <div class="deal-btn">Get this Deal</div>
    <div class="deal-sep"></div>
  </article>

  <article class="abs deal" style="top:637px">
    <div class="deal-photo" role="img" aria-label="Photo of white magnolia flowers in a torn paper frame"><i></i><span class="deal-caption">Cras turpis duis a<br>eget nulla vulput</span></div>
    <div class="deal-badge"><b>50%</b></div>
    <p class="deal-desc"><strong>Donec accumsan porta risus.</strong> Vestibulum sollicitudinlibero ut semper commodo, purus enim sollicitudin nulla, dictum vehicula diam lacus at purus. In egestas.</p>
    <h3 class="deal-heading">Services</h3>
    <div class="deal-link" style="top:82px">Nam congue quam non augue ivamus porttitor</div>
    <div class="deal-link" style="top:100px">Jam aongue buam n augue famus</div>
    <div class="deal-timer">30 : 15 : 15 : 06 <small>ago</small></div>
    <div class="deal-btn">Get this Deal</div>
    <div class="deal-sep"></div>
  </article>

  <article class="abs deal" style="top:819px">
    <div class="deal-photo" role="img" aria-label="Photo of white magnolia flowers in a torn paper frame"><i></i><span class="deal-caption">Cras turpis duis a<br>eget nulla vulput</span></div>
    <div class="deal-badge"><b>50%</b></div>
    <p class="deal-desc"><strong>Donec accumsan porta risus.</strong> Vestibulum sollicitudinlibero ut semper commodo, purus enim sollicitudin nulla, dictum vehicula diam lacus at purus. In egestas.</p>
    <h3 class="deal-heading">Services</h3>
    <div class="deal-link" style="top:82px">Nam congue quam non augue ivamus porttitor</div>
    <div class="deal-link" style="top:100px">Jam aongue buam n augue famus</div>
    <div class="deal-timer">30 : 15 : 15 : 06 <small>ago</small></div>
    <div class="deal-btn">Get this Deal</div>
    <div class="deal-sep"></div>
  </article>

  <nav class="abs pager">
    <span style="left:0;width:67px">&lsaquo; PREV</span>
    <span style="left:76px;width:22px">1</span>
    <span style="left:108px;width:22px">2</span>
    <span style="left:139px;width:22px">3</span>
    <span class="current" style="left:170px;width:22px">4</span>
    <span style="left:202px;width:22px">5</span>
    <span style="left:234px;width:22px">. . .</span>
    <span style="left:266px;width:22px">21</span>
    <span style="left:298px;width:22px">22</span>
    <span style="left:329px;width:22px">23</span>
    <span style="left:362px;width:22px">24</span>
    <span style="left:395px;width:22px">25</span>
    <span style="left:425px;width:66px">NEXT &rsaquo;</span>
  </nav>
</main>

<div class="abs divider"></div>

<aside>
  <h2 class="abs ribbon ribbon-right" style="top:410px;padding-left:59px">Categories
    <svg style="position:absolute;left:200px;top:10px" width="22" height="22" viewBox="0 0 22 22"><circle cx="11" cy="11" r="10" fill="#fff" stroke="#9c0a3a"/><path d="M7 9l4-4 4 4zM7 13l4 4 4-4z" fill="#d0104f"/></svg>
  </h2>
  <ul class="abs cat-list">
    <li><span class="cat-icon" style="background:#1c8fd6"></span>Restaurants</li>
    <li><span class="cat-icon" style="background:#8a2a9a"></span>Shopping</li>
    <li><span class="cat-icon" style="background:#444"></span>Events &amp; Attractions</li>
    <li><span class="cat-icon" style="background:#1aa8a0"></span>Hotels</li>
    <li><span class="cat-icon" style="background:#e0368a"></span>Health &amp; Beauty</li>
  </ul>

  <h2 class="abs ribbon ribbon-right" style="top:610px">Location</h2>
  <div class="abs" style="left:733px;top:660px;width:11px;height:11px;border:1px solid #999;background:#eee"></div>
  <div class="abs small-label" style="left:751px;top:661px">Include national</div>
  <div class="abs field select" style="left:731px;top:683px;width:152px;height:17px;line-height:15px">London (16)</div>
  <div class="abs small-label" style="left:737px;top:710px">Max Distance : <b>50km</b></div>
  <div class="abs tiny-btn" style="left:836px;top:709px;width:44px;height:13px">Submit</div>
  <div class="abs slider" style="left:731px;top:729px;width:136px"><i></i></div>

  <h2 class="abs ribbon ribbon-right" style="top:747px;padding-left:46px">Deals</h2>
  <div class="abs field select" style="left:731px;top:801px;width:150px;height:17px;line-height:15px">Order by distance</div>
  <div class="abs field select" style="left:731px;top:824px;width:150px;height:17px;line-height:15px">10 Deals per page</div>
  <div class="abs small-label" style="left:739px;top:847px">Price Range :</div>
  <div class="abs slider" style="left:731px;top:863px;width:136px"><i></i></div>
  <div class="abs field" style="left:731px;top:880px;width:150px;height:17px;line-height:15px">Mentioning</div>
  <div class="abs field" style="left:731px;top:903px;width:150px;height:17px;line-height:15px">Not Mentioning</div>

  <h2 class="abs ribbon ribbon-right" style="top:926px;padding-left:37px">Contact</h2>
  <div class="abs field placeholder" style="left:727px;top:972px;width:152px;height:17px;line-height:15px">Name</div>
  <div class="abs field placeholder" style="left:727px;top:993px;width:152px;height:17px;line-height:15px">e-mail</div>
  <div class="abs field placeholder" style="left:727px;top:1013px;width:152px;height:30px;line-height:18px">Message</div>
  <div class="abs go-btn">GO</div>
</aside>

<footer class="abs site-footer">
  <div class="foot-col" style="left:23px"><h4>ABOUT US</h4><ul><li>Company Information</li><li>Media Centre</li><li>Terms and conditions</li><li>Privacy Policy</li><li>Fair Use Policy</li><li>Contact us</li></ul></div>
  <div class="foot-col" style="left:146px"><h4>PRODUCTS</h4><ul><li>Home Monitoring</li><li>Holiday Monitoring</li><li>Small Business Monitoring</li><li>Wireless Alarm System</li><li>Prepaid Alarm Monitoring</li></ul></div>
  <div class="foot-col" style="left:286px"><h4>POPULAR PAGES</h4><ul><li>Check before your enter</li><li>Global Alerts</li><li>Anywhere access</li><li>Free Monitoring</li><li>Sign up</li></ul></div>
  <div class="foot-col" style="left:438px"><h4>CONNECT WITH US</h4>
    <div class="social"><span style="background:#3b5b99"></span><span style="background:#3fb0e8"></span><span style="background:#f28a1d"></span><span style="background:#ddd"></span></div>
  </div>
  <div class="foot-col" style="left:597px"><h4>NEWS LETTER</h4></div>
  <div class="news-input"></div>
  <div class="news-btn">Submit</div>
  <div class="copyright">Copyright © 2011.www.tukamoro.com</div>
</footer>

</body>
</html>
```